New Zealand Export company needs business cards

We need new business cards to match our new logo for a company based in New Zealand who deal specifically with the Pacific Islands. We source, consolidate and ship products out of New Zealand to the Pacific Islands. Will attach our old ones and also new logo.
Would like the Islands we deal with and the areas of work we have access to, to be included on the business cards.

Contact Information for Business Card

T +64 9 571 3048
F +64 9 571 6285
12-18 Kowhai Lane, Drury, 2113
PO Box 814, Drury, Auckland 2247, New Zealand
www.falconfreight.example.nz
E sales@falconfreight.example.nz

Font styles to use
Sans Serif

Colors
85abd2
33a6d7
ffffff

Requirements
Must have
• A company of PWM

```html
<!DOCTYPE html>
<html lang="en">
<head>
<meta charset="UTF-8">
<title>Falcon Freight – Business Card</title>
<link href="https://fonts.googleapis.com/css2?family=Lato:wght@400;700;900&display=swap" rel="stylesheet">
<style>
  :root {
    --navy: #0a57a4;
    --sky: #33a6d7;
    --soft-blue: #85abd2;
    --ink: #3c3c3c;
    --white: #ffffff;
    --backdrop: #e9ecef;
    --ghost: #eef0f6;
  }
  * { margin: 0; padding: 0; box-sizing: border-box; }
  html, body {
    width: 1200px; height: 1200px; overflow: hidden;
    background: var(--backdrop);
    font-family: "Lato", sans-serif;
  }
  .card {
    position: absolute;
    left: 265px;
    width: 670px;
    height: 390px;
    overflow: hidden;
    box-shadow: 0 4px 14px rgba(0,0,0,0.18);
  }
  .card-front { top: 166px; background: var(--white); }
  .card-back { top: 606px; background: var(--navy); }

  .brand {
    position: absolute;
    display: flex; align-items: center;
    font-family: "Lato", sans-serif;
    font-weight: 900;
    text-transform: uppercase;
    white-space: nowrap;
  }
  .brand-mark { display: block; flex: none; }
  .front-brand {
    top: 46px; left: 0; right: 0; justify-content: center;
    gap: 14px; letter-spacing: 2px;
    font-size: 44px; color: var(--navy);
  }
  .front-brand .brand-mark { width: 40px; height: 40px; background: var(--sky); }
  .back-brand {
    top: 172px; left: 330px; right: 30px; justify-content: center;
    gap: 10px; letter-spacing: 1px;
    font-size: 27px; line-height: 36px; color: var(--white);
  }
  .back-brand .brand-mark { width: 24px; height: 24px; background: var(--white); }

  .ghost-block {
    position: absolute;
    left: 365px; top: 138px; width: 305px; height: 172px;
    background: var(--ghost);
  }

  .company-name {
    position: absolute; left: 33px; top: 128px;
    font-size: 28px; font-weight: 700; color: var(--navy);
  }
  .contact-list {
    position: absolute; left: 33px; top: 196px;
    list-style: none;
  }
  .contact-list li {
    display: flex; align-items: center; gap: 7px;
    height: 24px;
    font-size: 21px; color: var(--ink);
  }
  .contact-icon { width: 19px; height: 19px; flex: none; }
  .address {
    position: absolute; left: 33px; top: 318px;
    font-size: 21px; line-height: 23px; color: var(--ink);
  }

  .scene-art { position: absolute; left: 0; top: 0; }
</style>
</head>
<body>

<section class="card card-front">
  <div class="ghost-block" aria-hidden="true"></div>

  <div class="brand front-brand">
    <span class="brand-mark"></span>
    <span>Falcon Freight</span>
  </div>

  <h1 class="company-name">Falcon Freight</h1>

  <ul class="contact-list">
    <li>
      <svg class="contact-icon" viewBox="0 0 20 20"><circle cx="10" cy="10" r="10" fill="var(--navy)"/><path d="M6.5 5.5l2 0 1 2.5-1.3 1a6 6 0 0 0 2.8 2.8l1-1.3 2.5 1 0 2a1 1 0 0 1-1 1A8.5 8.5 0 0 1 5.5 6.5a1 1 0 0 1 1-1z" fill="#fff"/></svg>
      <span>+64 9 571 3048</span>
    </li>
    <li>
      <svg class="contact-icon" viewBox="0 0 20 20"><circle cx="10" cy="10" r="10" fill="var(--navy)"/><rect x="7" y="4.5" width="6" height="4" fill="#fff"/><rect x="5" y="8" width="10" height="5" rx="1" fill="#fff"/><rect x="7" y="11" width="6" height="4.5" fill="#fff" stroke="var(--navy)" stroke-width="1"/></svg>
      <span>+64 9 571 6285</span>
    </li>
    <li>
      <svg class="contact-icon" viewBox="0 0 20 20"><circle cx="10" cy="10" r="10" fill="var(--navy)"/><rect x="5" y="6.5" width="10" height="7" fill="#fff"/><path d="M5 6.5l5 4 5-4" fill="none" stroke="var(--navy)" stroke-width="1.2"/></svg>
      <span>E sales@falconfreight.example.nz</span>
    </li>
    <li>
      <svg class="contact-icon" viewBox="0 0 20 20"><circle cx="10" cy="10" r="10" fill="var(--navy)"/><g fill="none" stroke="#fff" stroke-width="1"><circle cx="10" cy="10" r="5.5"/><ellipse cx="10" cy="10" rx="2.3" ry="5.5"/><path d="M4.5 10h11M5.3 7.3h9.4M5.3 12.7h9.4"/></g></svg>
      <span>www.falconfreight.example.nz</span>
    </li>
  </ul>

  <p class="address">
    12-18 Kowhai Lane, Drury, 2113<br>
    PO Box 814, Drury, Auckland 2247, New Zealand
  </p>
</section>

<section class="card card-back">
  <svg class="scene-art" width="670" height="390" viewBox="0 0 670 390">
    <defs>
      <linearGradient id="island-tones" x1="0" y1="0" x2="0" y2="1">
        <stop offset="0" stop-color="#2a7fc8"/>
        <stop offset="0.45" stop-color="#4f9a8e"/>
        <stop offset="0.7" stop-color="#3fb7d9"/>
        <stop offset="1" stop-color="#2fc0e6"/>
      </linearGradient>
    </defs>
    <path role="img" aria-label="Tropical island photo: palm trees, a stilt hut and a ship on turquoise water"
          d="M0 0H283Q345 195 280 390H0Z" fill="url(#island-tones)"/>
    <path d="M283 0Q345 195 280 390" fill="none" stroke="var(--white)" stroke-width="3"/>
  </svg>

  <div class="brand back-brand">
    <span class="brand-mark"></span>
    <span>Falcon Freight</span>
  </div>
</section>

</body>
</html>
```